Lorna Tess Tresses Fancy Business Card’s

I want my business cards to be elite, original and very classy. I want the business cards to match the colors of my logo and to match the design posted. I would love the design of the picture I posted

I want the card all white .
The dripping on the top of the card I want it to match the pink color in my logo that’s also posted .
I need my logo on the business card !
I need my Instagram- @lorna.tess.tresses__
And my phone number - 582 907 3365

Target Market(s)

My target market is young woman age 23 to older woman to the age of 65
I want both older and younger women to love my design . I don’t want any cheap looking business cards

Industry/Entity Type

Hair And Beauty

Contact Information for Business Card

Add my logo
Add my Instagram- @lorna.tess.tresses__
My number - 582 907 3365
My website- www.lornatesstresses.example

Font styles to use
Serif
Script

Colors
ffffff
e667a6
e34298

Requirements
Must have
• The business cards must have my logo, my number , my website, and my Instagram!
Nice to have
• Nice to have glitter words that match my logo
• The business cards must look classy and mature
• I want them to be very unique!!
Should not have
• Should not have any colors that doesn’t match my logo ! This is very important! Please

```html
<!DOCTYPE html>
<html lang="en">
<head>
<meta charset="utf-8">
<title>Lorna Tess Tresses – Business Card</title>
<link rel="stylesheet" href="https://fonts.googleapis.com/css2?family=Tinos:wght@400;700&display=swap">
<style>
  :root {
    --page: #ffffff;
    --crop: #3a2b27;
    --marble-light: #fdfbf9;
    --marble-vein: #f3e2d6;
    --pink-soft: #fdd3ea;
    --pink-glitter: #f2a2b4;
    --pink-glitter-deep: #e9899f;
    --magenta: #e23be0;
    --band: #ffffff;
  }
  html, body {
    margin: 0;
    width: 1200px;
    height: 893px;
    overflow: hidden;
    background: var(--page);
  }
  .canvas { display: block; width: 1200px; height: 893px; }
  .crop-mark { stroke: var(--crop); stroke-width: 5; stroke-linecap: round; }
  .card-marble { fill: url(#marbleTone); }
  .card-band { fill: var(--band); filter: url(#softShadow); }
  .card-pink { fill: var(--pink-soft); }
  .card-glitter { fill: url(#glitterTone); }
  .brand-name {
    font-family: "Tinos", "Times New Roman", serif;
    font-weight: 700;
    font-size: 74px;
    fill: var(--magenta);
  }
  .contact-line {
    font-family: "Tinos", "Times New Roman", serif;
    font-weight: 400;
    font-size: 36px;
    fill: var(--magenta);
  }
  .social-square { fill: var(--magenta); }
</style>
</head>
<body>
<svg class="canvas" viewBox="0 0 1200 893" xmlns="http://www.w3.org/2000/svg">
  <defs>
    <linearGradient id="marbleTone" x1="0" y1="0" x2="1" y2="1">
      <stop offset="0" stop-color="var(--marble-light)"/>
      <stop offset="0.5" stop-color="var(--marble-vein)"/>
      <stop offset="1" stop-color="var(--marble-light)"/>
    </linearGradient>
    <linearGradient id="glitterTone" x1="0" y1="0" x2="1" y2="1">
      <stop offset="0" stop-color="var(--pink-glitter)"/>
      <stop offset="1" stop-color="var(--pink-glitter-deep)"/>
    </linearGradient>
    <filter id="softShadow" x="-10%" y="-10%" width="120%" height="120%">
      <feDropShadow dx="-4" dy="4" stdDeviation="8" flood-color="#c9b9b4" flood-opacity="0.45"/>
    </filter>
    <clipPath id="cardClip"><rect x="144" y="179" width="898" height="532"/></clipPath>
  </defs>

  <g class="crop-marks">
    <line class="crop-mark" x1="170" y1="91" x2="170" y2="174"/>
    <line class="crop-mark" x1="61" y1="204" x2="141" y2="204"/>
    <line class="crop-mark" x1="1045" y1="682" x2="1111" y2="682"/>
    <line class="crop-mark" x1="1009" y1="716" x2="1009" y2="773"/>
  </g>

  <g class="card" clip-path="url(#cardClip)">
    <rect class="card-marble" x="144" y="179" width="898" height="532" role="img" aria-label="White marble texture with soft peach veins"/>
    <polygon class="card-band" points="560,179 1042,179 1042,620 1000,711 780,711"/>
    <polygon class="card-pink" points="588,179 1042,179 1042,583"/>
    <polygon class="card-glitter" points="980,520 1042,583 1042,711 806,711" role="img" aria-label="Pink glitter texture"/>

    <text class="brand-name" x="600" y="392" text-anchor="middle">Lorna Tess</text>
    <text class="brand-name" x="600" y="472" text-anchor="middle">Tresses</text>

    <rect class="social-square" x="412" y="540" width="34" height="34" rx="7"/>
    <text class="contact-line" x="458" y="569">@lorna.tess.tresses__</text>
    <text class="contact-line" x="592" y="620" text-anchor="middle">Phone: 582-907-3365</text>
    <text class="contact-line" x="592" y="668" text-anchor="middle">www.lornatesstresses.example</text>
  </g>
</svg>
</body>
</html>
```